Q7 Teaser

One page teaser for our business information and model. A financial service SPV platform.

Target Market(s)

Financial Professionals

Industry/Entity Type

Financial Service

Font styles to use
Sans Serif

Colors
ffcf3e
ffffff
cfcfcf
9d9d9d
aaaaaa
fbed22
ffc214
fee18a
fbee3f

Requirements
Must have
• Unique appearance of USPs.
• Important claims: Low Cost. First Class.
• and: We liberate the buy-side from the sell-side
Nice to have
• maybe keyword cloud

```html
<!DOCTYPE html>
<html lang="en">
<head>
<meta charset="utf-8">
<title>Q7 Teaser</title>
<link rel="stylesheet" href="https://fonts.googleapis.com/css2?family=Montserrat:wght@600;700&family=Didact+Gothic&family=Cinzel:wght@400;600&display=swap">
<style>
  :root {
    --gold: #cc9a2c;
    --gold-deep: #b8861f;
    --gold-soft: #fee18a;
    --ink: #3f3f3f;
    --charcoal: #555555;
    --panel: #ececec;
    --white: #ffffff;
    --stage: #e6e6e6;
    --grey-mid: #9d9d9d;
  }
  * { box-sizing: border-box; margin: 0; padding: 0; }
  html, body { width: 1041px; height: 1200px; overflow: hidden; background: var(--stage); }
  .flyer {
    position: absolute; left: 103px; top: 10px;
    width: 766px; height: 1082px;
    transform: scale(1.09); transform-origin: top left;
    background: var(--white);
    font-family: "Didact Gothic", sans-serif;
    color: var(--ink);
    overflow: hidden;
  }
  .hero { position: absolute; left: 0; top: 0; width: 766px; height: 472px; overflow: hidden; }
  .hero-photo {
    position: absolute; inset: 0;
    background:
      radial-gradient(ellipse 180px 200px at 230px 260px, #8a7550 0%, rgba(138,117,80,0) 100%),
      radial-gradient(ellipse 200px 160px at 150px 140px, #7a9a3c 0%, rgba(122,154,60,0) 100%),
      linear-gradient(180deg, #6f7d3c 0%, #c8b874 45%, #e6d59a 62%, #9c7f57 78%, #6d5a43 100%);
  }
  .hero-photo::after {
    content: ""; position: absolute; inset: 0;
    background: linear-gradient(90deg, rgba(255,255,255,0) 40%, rgba(255,246,220,0.55) 100%);
  }
  .brand {
    position: absolute; right: 30px; top: 46px;
    display: flex; align-items: center; gap: 12px;
  }
  .brand-dot { width: 44px; height: 44px; border-radius: 50%; background: var(--gold); }
  .brand-name {
    font-family: "Didact Gothic", sans-serif; color: var(--gold);
    font-size: 30px; letter-spacing: 1px;
  }
  .claim-disc {
    position: absolute; left: 434px; top: 160px;
    width: 340px; height: 340px; border-radius: 50%;
    background: radial-gradient(circle at 40% 40%, rgba(196,140,30,0.95), rgba(176,122,22,0.92));
  }
  .claim {
    position: absolute; left: 470px; top: 232px; width: 280px;
    text-align: center; color: var(--white);
  }
  .claim-title {
    font-family: "Montserrat", sans-serif; font-weight: 700;
    font-size: 41px; line-height: 48px; letter-spacing: 0.5px;
  }
  .claim-line { font-size: 25px; line-height: 29px; margin-top: 12px; }
  .tagline {
    position: absolute; left: 0; top: 472px; width: 766px; height: 46px;
    background: var(--gold); color: var(--white);
    font-family: "Montserrat", sans-serif; font-weight: 700;
    font-size: 23px; line-height: 46px; text-align: center; letter-spacing: 0.2px;
  }
  .intro {
    position: absolute; left: 0; top: 518px; width: 766px; height: 131px;
    background: var(--charcoal); color: var(--white);
    padding: 12px 36px 0 37px;
    font-size: 12.4px; line-height: 15.4px; text-align: justify;
  }
  .usp { position: absolute; left: 0; top: 649px; width: 400px; height: 331px; padding: 16px 0 0 37px; }
  .usp-title {
    font-family: "Montserrat", sans-serif; font-weight: 700;
    color: var(--gold); font-size: 38px; line-height: 38px;
  }
  .usp-sub { font-size: 17px; line-height: 18px; color: var(--ink); margin-top: 4px; }
  .keyword-cloud {
    position: absolute; left: 64px; top: 36px; width: 320px; height: 205px;
    font-family: "Cinzel", serif; text-align: center; line-height: 1;
  }
  .kw { display: block; white-space: nowrap; }
  .kw-gold { color: var(--gold); }
  .kw-ink { color: #555; }
  .about {
    position: absolute; left: 37px; top: 260px; width: 350px;
    font-size: 12.4px; line-height: 14.6px; color: var(--ink);
  }
  .products {
    position: absolute; left: 400px; top: 649px; width: 366px; height: 331px;
    background: var(--panel); padding: 16px 0 0 28px;
  }
  .products-title {
    font-family: "Montserrat", sans-serif; font-weight: 700;
    color: var(--gold); font-size: 25px; line-height: 30px;
  }
  .products-sub { font-size: 20px; line-height: 24px; color: var(--ink); margin-bottom: 14px; }
  .product-list { list-style: none; }
  .product-list li {
    display: flex; align-items: center; gap: 8px;
    font-size: 16px; line-height: 23.5px; color: var(--ink);
  }
  .tick { width: 10px; height: 10px; flex: none; }
  .cta {
    position: absolute; left: 0; top: 980px; width: 766px; height: 50px;
    background: var(--charcoal); color: var(--white);
    text-align: center; line-height: 52px; font-size: 27px;
  }
  .cta strong { font-family: "Montserrat", sans-serif; font-weight: 700; font-size: 26px; }
  .contact {
    position: absolute; left: 0; top: 1030px; width: 766px; height: 52px;
    background: var(--gold); color: var(--white);
    display: flex; justify-content: center; align-items: center; gap: 34px;
    font-size: 17px;
  }
  .contact-item { display: flex; align-items: center; gap: 8px; }
  .contact-phone { font-family: "Montserrat", sans-serif; font-weight: 700; font-size: 21px; }
  .contact svg { width: 14px; height: 14px; fill: var(--white); }
</style>
</head>
<body>
<main class="flyer">
  <section class="hero">
    <div class="hero-photo" role="img" aria-label="Glass jar filled with coins and a young green plant sprouting from it, on a wooden table with a soft sunlit background"></div>
    <div class="brand">
      <span class="brand-dot"></span>
      <span class="brand-name">Q7 Financial Products</span>
    </div>
    <div class="claim-disc"></div>
    <div class="claim">
      <div class="claim-title">LOW COST<br>FIRST CLASS</div>
      <p class="claim-line">We democratise structured financial product issuance.</p>
    </div>
  </section>

  <h1 class="tagline">WE LIBERATE THE BUY-SIDE FROM THE SELL-SIDE.</h1>

  <p class="intro">We serve our clients with the power to create their own branded, tailor-made financial products and investment solutions by providing them with right tools and structures to establish and operate first class off-balance sheet issuance vehicles (SPV). We create unique solutions to expand your business reach, services and qualities by liberating financial product issuance to buy-side. Asset owners, distributers and managers are given the full capability to securitise their own asset base in unlimited capacity, outside their balance sheet with customisable transparency and counterparty risk. A clear and simple solutions to serve your best interests and without the need for conventional sell-side issuers.</p>

  <section class="usp">
    <h2 class="usp-title">YOUR</h2>
    <p class="usp-sub">BRAND. REWARD.<br>SOLUTION.</p>
    <div class="keyword-cloud" aria-label="Keyword cloud">
      <span class="kw kw-ink" style="font-size:13px;margin-left:60px">Various</span>
      <span class="kw kw-gold" style="font-size:14px">Quick Setup</span>
      <span class="kw kw-gold" style="font-size:10px">Your own fee policy</span>
      <span class="kw kw-ink" style="font-size:12px">Low cost structure</span>
      <span class="kw kw-gold" style="font-size:16px">Shore&nbsp; Daily Liquidity</span>
      <span class="kw kw-ink" style="font-size:20px">Open Architecture</span>
      <span class="kw kw-ink" style="font-size:18px">Swiss Paying Agent</span>
      <span class="kw kw-gold" style="font-size:13px">Regulatory Compliant (MiFID)</span>
      <span class="kw kw-gold" style="font-size:10px">Customised Transparency</span>
      <span class="kw kw-gold" style="font-size:24px">Off-Balance Sheet</span>
      <span class="kw kw-ink" style="font-size:15px">Own Issuance Vehicle (SPV)</span>
      <span class="kw kw-gold" style="font-size:13px">Various Off-Shore Locations</span>
      <span class="kw kw-ink" style="font-size:8px">Investment &amp; risk control</span>
    </div>
    <p class="about">Q7 Financial Product AG is a financial service provider built on the unique experience and robust track record of its team. Our founders gathered the most qualified experts to benefit our clients and business partners.</p>
  </section>

  <section class="products">
    <h2 class="products-title">GROW YOUR BUSINESS</h2>
    <p class="products-sub">OFFER YOUR PRODUCTS:</p>
    <ul class="product-list">
      <li><svg class="tick" viewBox="0 0 10 10"><path d="M1 5.5 L4 8.5 L9 1.5" fill="none" stroke="#cc9a2c" stroke-width="1.6"/></svg>Structured Products</li>
      <li><svg class="tick" viewBox="0 0 10 10"><path d="M1 5.5 L4 8.5 L9 1.5" fill="none" stroke="#cc9a2c" stroke-width="1.6"/></svg>Active Managed Certificate (AMC)</li>
      <li><svg class="tick" viewBox="0 0 10 10"><path d="M1 5.5 L4 8.5 L9 1.5" fill="none" stroke="#cc9a2c" stroke-width="1.6"/></svg>Static Trackers</li>
      <li><svg class="tick" viewBox="0 0 10 10"><path d="M1 5.5 L4 8.5 L9 1.5" fill="none" stroke="#cc9a2c" stroke-width="1.6"/></svg>Securitisation of depth</li>
      <li><svg class="tick" viewBox="0 0 10 10"><path d="M1 5.5 L4 8.5 L9 1.5" fill="none" stroke="#cc9a2c" stroke-width="1.6"/></svg>Crypto-backed securities</li>
      <li><svg class="tick" viewBox="0 0 10 10"><path d="M1 5.5 L4 8.5 L9 1.5" fill="none" stroke="#cc9a2c" stroke-width="1.6"/></svg>Trade Financial</li>
      <li><svg class="tick" viewBox="0 0 10 10"><path d="M1 5.5 L4 8.5 L9 1.5" fill="none" stroke="#cc9a2c" stroke-width="1.6"/></svg>Asset backed Sec.</li>
      <li><svg class="tick" viewBox="0 0 10 10"><path d="M1 5.5 L4 8.5 L9 1.5" fill="none" stroke="#cc9a2c" stroke-width="1.6"/></svg>Privat Equity Finance</li>
      <li><svg class="tick" viewBox="0 0 10 10"><path d="M1 5.5 L4 8.5 L9 1.5" fill="none" stroke="#cc9a2c" stroke-width="1.6"/></svg>Insurance Linked Securities</li>
      <li><svg class="tick" viewBox="0 0 10 10"><path d="M1 5.5 L4 8.5 L9 1.5" fill="none" stroke="#cc9a2c" stroke-width="1.6"/></svg>Leverage Products</li>
    </ul>
  </section>

  <p class="cta"><strong>CONTACT US TODAY</strong> FOR ANY CONSULTATION</p>

  <footer class="contact">
    <span class="contact-item contact-phone">
      <svg viewBox="0 0 14 14"><path d="M3 1 L5 1 L6 4 L4.5 5.2 Q6 8 8.8 9.5 L10 8 L13 9 L13 11 Q13 13 11 13 Q1 12 1 3 Q1 1 3 1Z"/></svg>123-456-789
    </span>
    <span class="contact-item">
      <svg viewBox="0 0 14 14"><circle cx="7" cy="7" r="5.5" fill="none" stroke="#fff" stroke-width="1.4"/><path d="M1.5 7 H12.5 M7 1.5 Q3.5 7 7 12.5 M7 1.5 Q10.5 7 7 12.5" fill="none" stroke="#fff" stroke-width="1"/></svg>www.q7-platform.example
    </span>
    <span class="contact-item">
      <svg viewBox="0 0 14 14"><rect x="1" y="3" width="12" height="8"/><path d="M1 3 L7 8 L13 3" fill="none" stroke="#cc9a2c" stroke-width="1"/></svg>info@q7-platform.example
    </span>
  </footer>
</main>
</body>
</html>
```